Gavin Unboxed - Album

Hi all

I am planning on releasing my first album for online distribution shortly. I have chosen the tracks that I want to put in it. You can listen to them through my set "Gavin Unboxed": http://tunehollow.net/thorneg/sets/gavin-unboxed

I am not particularly happy with the name "Gavin Unboxed", so I have created a competition to find a better album name. Anyone is welcome to enter. The best two entries will win a free copy of the album when it comes out:
http://tunehollow.net/thorneg/album-name
The album name competition will end on December 17.
If you have a design idea before that time, feel free to submit that as well as the album name. You can send as many ideas as you like.
After the album name is decided upon, this will be like a normal design competition.
I am planning on distributing the album online through VexaSonic.
According to vexasonic.net: "Submitted cover art must be 1500 x 1500 pixels jpg. It cannot be blurry or pixilated and must be perfectly square."
The artwork should probably contain something like "by Gavin Thorne" as well as the title.
VexaSonic make choose to make a CD version of the album, but I believe they use the .jpg file to generate that.

Thanks in advance,
Gavin :)

A mosaic, patchwork or collage would be good, to reflect the variety of the music.

I have added a couple of photos that you may or may not want to use. One is of me, the other is of my "studio", most of which is my laptop. :)

I hope that helps. (now you know why I haven't included these already)

Hi everyone

Thanks to all those who entered.

I received many suggestions, and the decision was tough.

Eventually I decided on "Quirk Jangle" as the name.
It is the name of one of the pieces on the album: http://tunehollow.net/thorneg/quirkjangle

Hopefully this will draw in the audience that will appreciate my quirky music.

The runners up were "Far Echoes" and "Dusk Lantern". Both of these two were submitted by Pixel Harbor participants.
I will organise a copy of the album to be sent to those people once the album comes out.

For background, the "Quirk" part of the name was from the musical concept of a mode, being an arrangement of a series of notes (scale). "Jangle" was my way of expressing a dismissive attitude to that - sort of like "Who needs conventional music theory".

Thanks again,
and good luck with the designs,
Gavin :)

Target Market(s)

People who buy music online. My music covers a wide range.

Industry/Entity Type

Online

```html
<!DOCTYPE html>
<html lang="en">
<head>
<meta charset="utf-8">
<title>Quirk Jangle — Gavin Thorne</title>
<link rel="stylesheet" href="https://fonts.googleapis.com/css2?family=Alfa+Slab+One&display=swap">
<style>
  :root {
    --ink: #0b0b0b;
    --paper: #ffffff;
    --gap: 6px;
    --letter-font: "Alfa Slab One", serif;
  }
  html, body {
    margin: 0;
    padding: 0;
    overflow: hidden;
    background: var(--ink);
  }
  .album-cover {
    width: 1186px;
    height: 1200px;
    box-sizing: border-box;
    padding: var(--gap);
    background: var(--ink);
    display: grid;
    grid-template-columns: repeat(7, 1fr);
    grid-template-rows: repeat(7, 1fr);
    gap: var(--gap);
  }
  .tile {
    overflow: hidden;
    min-width: 0;
    min-height: 0;
  }
  .word-row {
    display: grid;
    gap: var(--gap);
  }
  .title-first { grid-column: 2 / 7; grid-template-columns: repeat(5, 1fr); }
  .title-second { grid-column: 2 / 7; grid-template-columns: repeat(6, 1fr); }
  .artist-first { grid-column: 2 / 7; grid-template-columns: repeat(5, 1fr); }
  .artist-last { grid-column: 1 / 8; grid-template-columns: repeat(6, 1fr); }

  .letter {
    display: flex;
    align-items: center;
    justify-content: center;
    font-family: var(--letter-font);
    font-size: 132px;
    line-height: 1;
    text-transform: lowercase;
    overflow: hidden;
  }
  .letter.capital { text-transform: none; }
  .letter.on-light { background: var(--paper); color: var(--ink); }
  .letter.on-dark { background: var(--ink); color: var(--paper); }
  .title-second .letter { font-size: 116px; }
  .artist-last .letter { font-size: 150px; }

  .photo { display: block; }
  .photo-fountain { background: linear-gradient(160deg, #8a8478, #4c4a44); }
  .photo-splash { background: radial-gradient(circle at 50% 55%, #e84a1c, #a8d42a 45%, #5fae2c 80%); }
  .photo-bagpipes { background: radial-gradient(circle at 50% 55%, #c4222a, #f4efe8 70%); }
  .photo-rings { background: radial-gradient(ellipse at 50% 50%, #d2843a, #f6f1ea 65%); }
  .photo-laptop { background: linear-gradient(180deg, #3a3d42, #7b7f86 60%, #c9c9c4); }
  .photo-sheet-music { background: linear-gradient(135deg, #f3f3f3, #cfcfcf); }
  .photo-barbed-wire { background: linear-gradient(180deg, #2a64c8, #6aa6ee); }
  .photo-dragon { background: radial-gradient(circle at 50% 50%, #3e6a6a, #f4f4f4 70%); }
  .photo-fractal { background: radial-gradient(circle at 50% 50%, #e6b428, #3b5a3a 55%, #1a1f2a); }
  .photo-rocket { background: linear-gradient(180deg, #8fb6d8, #d7dde2 70%, #c89a6a); }
  .photo-buried-block { background: linear-gradient(180deg, #4f6a3a, #e4e8ee 50%, #5a4330); }
  .photo-cap { background: radial-gradient(circle at 50% 45%, #ffffff, #d8d8d8 60%, #222 100%); }
  .photo-dance-poster { background: linear-gradient(180deg, #8b6a2a, #c94a2a 55%, #6a4a1a); }
  .photo-cookies { background: radial-gradient(circle at 45% 55%, #b88a5a, #d9c6a4 60%, #9fb4a4); }
  .photo-galaxy { background: radial-gradient(circle at 50% 50%, #9a4cc4, #1e2a6a 55%, #05060f); }
  .photo-flowers { background: radial-gradient(circle at 40% 60%, #e4473a, #e9a24a 50%, #d9c7b8); }
  .photo-cave { background: linear-gradient(180deg, #3a2e22, #8c7658 60%, #5a4a36); }
  .photo-crossed-score { background: linear-gradient(135deg, #ffffff, #e9e3e6); }
  .photo-astronaut { background: linear-gradient(180deg, #101010, #3a3a3a 45%, #9a9a94); }
  .photo-cartoon { background: radial-gradient(circle at 50% 45%, #7a4ab8, #2e3fae 60%, #f4f4f4 61%); }
  .photo-keys { background: linear-gradient(135deg, #f2f2f2, #1a1a1a 70%); }
  .photo-panpipes { background: linear-gradient(180deg, #ffffff, #e0572a 45%, #2a7ac0 60%, #ffffff); }
  .photo-storm { background: linear-gradient(180deg, #2a3140, #6a7a8c 55%, #23303c); }
  .photo-armchair { background: radial-gradient(circle at 50% 55%, #7a6a4a, #f6f6f6 70%); }
  .photo-car-interior { background: linear-gradient(180deg, #e6e8ea, #2c2e30 55%, #121314); }
  .photo-headphones { background: radial-gradient(circle at 50% 55%, #2a2a2a, #ffffff 62%); }
  .photo-portrait { background: linear-gradient(160deg, #ffffff, #bdbdbd); }
</style>
</head>
<body>
<main class="album-cover" aria-label="Quirk Jangle by Gavin Thorne">
  <!-- Row 1 -->
  <div class="tile photo photo-fountain" role="img" aria-label="Photo of an old stone fountain archway"></div>
  <h1 class="tile word-row title-first" aria-label="Quirk" style="margin:0">
    <span class="letter capital on-light">Q</span>
    <span class="letter on-dark">u</span>
    <span class="letter on-light">i</span>
    <span class="letter on-dark">r</span>
    <span class="letter on-light">k</span>
  </h1>
  <div class="tile photo photo-splash" role="img" aria-label="Abstract green and orange paint splash"></div>

  <!-- Row 2 -->
  <div class="tile photo photo-bagpipes" role="img" aria-label="Tartan bagpipes"></div>
  <div class="tile word-row title-second" aria-label="Jangle">
    <span class="letter capital on-dark">J</span>
    <span class="letter on-light">a</span>
    <span class="letter on-dark">n</span>
    <span class="letter on-light">g</span>
    <span class="letter on-dark">l</span>
    <span class="letter on-light">e</span>
  </div>
  <div class="tile photo photo-rings" role="img" aria-label="Two gold wedding rings"></div>

  <!-- Row 3 -->
  <div class="tile photo photo-laptop" role="img" aria-label="Laptop running music software"></div>
  <div class="tile photo photo-sheet-music" role="img" aria-label="Pages of sheet music"></div>
  <div class="tile photo photo-barbed-wire" role="img" aria-label="Coiled barbed wire against blue sky"></div>
  <div class="tile photo photo-dragon" role="img" aria-label="Toy dragon figure"></div>
  <div class="tile photo photo-fractal" role="img" aria-label="Colourful fractal spiral"></div>
  <div class="tile photo photo-rocket" role="img" aria-label="Rocket lifting off"></div>
  <div class="tile photo photo-buried-block" role="img" aria-label="White block in a dug hole in grass"></div>

  <!-- Row 4 -->
  <div class="tile photo photo-cap" role="img" aria-label="Cap with a marching band warning sign"></div>
  <div class="tile photo photo-dance-poster" role="img" aria-label="Retro dance poster with a dancing couple"></div>
  <div class="tile photo photo-cookies" role="img" aria-label="Cookies on a plate"></div>
  <div class="tile photo photo-galaxy" role="img" aria-label="Colliding galaxies in space"></div>
  <div class="tile photo photo-flowers" role="img" aria-label="Orange and red marigold flowers"></div>
  <div class="tile photo photo-cave" role="img" aria-label="Cave mouth with rocky floor"></div>
  <div class="tile photo photo-crossed-score" role="img" aria-label="Musical score crossed out in pink"></div>

  <!-- Row 5 -->
  <div class="tile photo photo-astronaut" role="img" aria-label="Astronaut standing on the moon"></div>
  <div class="tile photo photo-cartoon" role="img" aria-label="Purple cartoon creature in a blue circle"></div>
  <div class="tile photo photo-keys" role="img" aria-label="Piano keys in high contrast"></div>
  <div class="tile photo photo-panpipes" role="img" aria-label="Colourful pan pipes"></div>
  <div class="tile photo photo-storm" role="img" aria-label="Storm clouds over the sea"></div>
  <div class="tile photo photo-armchair" role="img" aria-label="Plaid armchair"></div>
  <div class="tile photo photo-car-interior" role="img" aria-label="Car dashboard and steering wheel"></div>

  <!-- Row 6 -->
  <div class="tile photo photo-headphones" role="img" aria-label="Studio headphones"></div>
  <div class="tile word-row artist-first" aria-label="Gavin">
    <span class="letter capital on-light">G</span>
    <span class="letter on-dark">a</span>
    <span class="letter on-light">v</span>
    <span class="letter on-dark">i</span>
    <span class="letter on-light">n</span>
  </div>
  <div class="tile photo photo-portrait" role="img" aria-label="Black and white portrait of the artist"></div>

  <!-- Row 7 -->
  <div class="tile word-row artist-last" aria-label="Thorne">
    <span class="letter capital on-dark">T</span>
    <span class="letter on-light">h</span>
    <span class="letter on-dark">o</span>
    <span class="letter on-light">r</span>
    <span class="letter on-dark">n</span>
    <span class="letter on-light">e</span>
  </div>
</main>
</body>
</html>
```